i NEED A MY CURRENT LOGO UPDATED TO MAKE IT LOOK MORE MODERN. I WANT TO KEEP MY CURRENT COLOURS FOR THE LOGO WHICH ARE GREEN, BLACK, WHITE AND SILVER/METALIC COLOURS.

I RUN A BUSINESS WHICH IS CALLED "CONVEYANCING" IN AUSTRALIA. THIS BUSINESS PROVIDES A SERVICES FOR PEOPLE WHO ARE BUYING OR SELLING OR TRANSFER THEIR PROPERTY. WE ARE NOT A REAL ESTATE AGENT. WE PREPARE AND DO ALL WORK NECESSARY TO COMPLETE A LEGAL TRANSFER OF PROPERTY FOR CUSTOMERS. THE REASON i CHOSE THE NAME "KOREVAN CONVEYANCING" IS BECAUSE WE CAN ONLY DO VICTORIAN PROPERTY TRANSFERS AND IN AUSTRALIA THE LAND IS TRANSFERED TO AN OWNER AND WHATEVER IS ON THE LAND BECOMES THE OWNERS.

MY LOGO MUST HAVE THE VICTORIAN STATE AS A SYMBOL (VICTORIA IS ONE OF THE STATES IN AUSTRALIA AND IT'S KNOWN AS A GREEN STATE). I CAN EMAIL YOU THE CURRENT LOGO TO GIVE YOU AN IDEA.

I'M HAPPY WITH THE CURRENT COLOURS BUT NOT THE LAYOUT OR DESIGN. AT THE MOMENT IT'S PRETTY PLAIN AND BORING.

Example - This is a creative design I copied from the net.

Hi All, I've posted a design in which I would like you to consider being creative with the victorian logo as they have done with the swan here.  Just an idea.

Hi All, I just wanted to let you know that other than the colours I requested I want you all to come up with your own idea of the logo.  So far this is the only create design I've seen. 

Target Market(s)

People that are in the market to buy or selling property/real estate.

Industry/Entity Type

Business

Requirements
Must have
• THE COLOURS MUST REMAIN THE SAME AND MUST BE PROFESSIONAL AS WE ARE A PART OF THE LEGAL (PROFESSIONAL)INDUSTRY IN AUSTRALIA
Nice to have
• MUST HAVE THE VICTORIAN LOGO/SYMBOL
Should not have
• SHOULD NOT BE BORING. THE DETAILS OF OUR ADDRESS ON THE ATTACHED IS OLD DETAILS NOT OUR CURRENT DETAILS. IT'S ATTACHED TO SHOW YOU AN EXAMPLE OF THE CURRENT LOGO.

```html
<!DOCTYPE html>
<html lang="en">
<head>
<meta charset="utf-8">
<title>Korevan Conveyancing – Business Cards</title>
<link rel="stylesheet" href="https://fonts.googleapis.com/css2?family=Arimo:wght@400;700&family=Roboto+Condensed:wght@700&display=swap">
<style>
  :root {
    --bg: #e9e9e6;
    --ink-black: #0c0c0c;
    --lime: #8fe31a;
    --lime-bright: #a4f21f;
    --lime-pale: #c4f36a;
    --lime-deep: #6fc20f;
    --white: #ffffff;
    --rule: #d8d8d8;
  }
  * { box-sizing: border-box; margin: 0; padding: 0; }
  html, body { width: 1200px; height: 1150px; overflow: hidden; }
  body { background: var(--bg); font-family: "Arimo", Arial, sans-serif; position: relative; }

  .card {
    position: absolute;
    left: 170px;
    width: 860px;
    height: 512px;
    overflow: hidden;
    box-shadow: 0 6px 18px rgba(0,0,0,0.18);
  }

  /* ---------- Front card ---------- */
  .card--front { top: 42px; background: var(--ink-black); }
  .front__block-top {
    position: absolute; left: 40px; top: 36px;
    width: 292px; height: 100px; background: var(--lime-bright);
  }
  .front__block-bottom {
    position: absolute; left: 40px; top: 320px;
    width: 346px; height: 192px; background: var(--lime-bright);
    overflow: hidden;
  }
  .state-map {
    position: absolute;
    background: linear-gradient(160deg, var(--lime-pale), rgba(196,243,106,0.55));
    border-radius: 40% 55% 30% 45% / 45% 35% 55% 40%;
  }
  .front__block-bottom .state-map { left: 10px; top: 20px; width: 260px; height: 110px; }

  .brand {
    position: absolute;
    display: flex; align-items: center; gap: 12px;
  }
  .brand__dot { border-radius: 50%; background: var(--lime); flex: none; }
  .brand__name {
    font-family: "Arimo", Arial, sans-serif; font-weight: 700;
    line-height: 1.05; letter-spacing: 0.5px;
  }
  .card--front .brand { left: 30px; top: 208px; }
  .card--front .brand__dot { width: 44px; height: 44px; }
  .card--front .brand__name { color: var(--white); font-size: 26px; }

  .holder {
    position: absolute; right: 40px; top: 26px; text-align: right;
  }
  .holder__name {
    font-family: "Roboto Condensed", "Arial Narrow", sans-serif;
    font-weight: 700; font-size: 42px; color: var(--lime-bright); line-height: 1;
  }
  .holder__address {
    font-size: 24px; color: var(--white); line-height: 1.25; margin-top: 4px;
  }
  .holder__rule {
    position: absolute; right: 40px; top: 136px;
    width: 440px; height: 2px; background: var(--rule);
  }

  .contact {
    position: absolute; left: 420px; top: 382px;
    list-style: none; font-size: 21px; line-height: 1.55;
  }
  .contact__label { color: var(--white); font-weight: 700; }
  .contact__value { color: var(--lime-bright); }

  /* ---------- Back card ---------- */
  .card--back {
    top: 596px;
    background: linear-gradient(135deg, var(--lime-bright) 0%, var(--lime) 60%, var(--lime-deep) 100%);
  }
  .card--back .state-map { left: 10px; top: 10px; width: 520px; height: 330px; opacity: 0.7; }
  .card--back .brand { left: 460px; top: 120px; }
  .card--back .brand__dot { width: 56px; height: 56px; background: var(--white); }
  .card--back .brand__name { color: var(--white); font-size: 32px; }

  .notices {
    position: absolute; left: 90px; top: 392px;
    list-style: none; color: var(--white); font-size: 19px; line-height: 1.4;
  }
  .notices li::before { content: "• "; }
</style>
</head>
<body>

  <section class="card card--front" aria-label="Business card front">
    <div class="front__block-top"></div>
    <div class="front__block-bottom">
      <div class="state-map" role="img" aria-label="Map silhouette of the state of Victoria"></div>
    </div>

    <div class="brand">
      <span class="brand__dot"></span>
      <span class="brand__name">KOREVAN<br>CONVEYANCING</span>
    </div>

    <div class="holder">
      <p class="holder__name">Lena Carrow</p>
      <p class="holder__address">14 Fenwick Avenue,<br>Ashwood Park Victoria 3070</p>
    </div>
    <div class="holder__rule"></div>

    <ul class="contact">
      <li><span class="contact__label">Tel:</span> <span class="contact__value">(03) 9400 1234</span></li>
      <li><span class="contact__label">Fax:</span> <span class="contact__value">(03) 9400 1235</span></li>
      <li><span class="contact__label">Email:</span> <span class="contact__value">korevanconveyancing@mailbox.com</span></li>
    </ul>
  </section>

  <section class="card card--back" aria-label="Business card back">
    <div class="state-map" role="img" aria-label="Large faint map silhouette of the state of Victoria"></div>

    <div class="brand">
      <span class="brand__dot"></span>
      <span class="brand__name">KOREVAN<br>CONVEYANCING</span>
    </div>

    <ul class="notices">
      <li>This firm holds professional indemnity insurance against civil liability.</li>
      <li>A solicitor is employed by this firm for all legal work.</li>
      <li>Professional Indemnity.</li>
    </ul>
  </section>

</body>
</html>
```